Professional Lighting Providers - Web Design

We need a web design to showcase our ability to provide lighting design and equipment to those who are in need of lighting equipment.

Our 4 markets are:
Broadcasting - Public and Commercial
Education - ISD wide, and private schools
Government - National News, Chamber videos, Press Releases
Religious - Sermon Recording, etc.

We provide lighting products, design consultations(how lights are setup and such), and custom light work.

We want the home page to be setup in a way that someone in one of the 4 markets can drill down into the site. Meaning they are greeted on the home page with 4 large icons or pictures for each market and then they can go farther into the site. We also want a top navigation to be preset so people who are just looking for lighting can also browse our products.

Logo colors are not as they appear on our current website.
#383388 is our current logo color, please also see attachment of logo. In addition, we are just "Bright Harbor - Lighting Systems". We dropped the RJ7 out of our name so please don't use it in the concept.

Our Current Site is http://rj7-example.com/index.asp.
We don't have set colors but we know we do not want reds or yellows.

The design should be simple, not cluttered, and not artsy, not fun, but very serious.

Requirements
Must have
• Image banner/slider at the top that slides our 4 products.
Also need to have a form on the home page that will convert visitors to subscribers for a newsletter. Also on every page we want a form were people can send an email off to us asking questions.

```html
<!DOCTYPE html>
<html lang="en">
<head>
<meta charset="utf-8">
<title>Bright Harbor - Lighting Systems</title>
<link href="https://fonts.googleapis.com/css2?family=Roboto+Condensed:wght@400;700&family=Arimo:wght@400;700&display=swap" rel="stylesheet">
<style>
:root{
  --brand:#383388;
  --brand-dark:#2a2670;
  --feature:#561f6e;
  --feature-dark:#3f1552;
  --card:#333333;
  --card-dark:#1f1f1f;
  --page:#efefef;
  --band:#e4e4e4;
  --text:#555555;
  --muted:#9a9a9a;
  --white:#ffffff;
}
*{box-sizing:border-box;margin:0;padding:0}
html,body{width:1200px;height:1107px;overflow:hidden}
body{position:relative;background:var(--page);font-family:Arimo,Arial,sans-serif;color:var(--text)}
.abs{position:absolute}
.cond{font-family:"Roboto Condensed",Arial Narrow,sans-serif;font-weight:700;text-transform:uppercase}

/* header */
.masthead{left:0;top:0;width:1200px;height:69px;background:linear-gradient(#fff,#f2f2f2);border-bottom:1px solid #d6d6d6}
.brand{left:162px;top:16px;display:flex;align-items:center;gap:8px}
.brand-mark{width:32px;height:32px;border-radius:50%;background:var(--brand)}
.brand-name{font-size:17px;font-weight:700;color:var(--brand);line-height:1.1}
.utility{left:781px;top:0;width:255px;height:23px;background:#3a3a3a;border-radius:0 0 3px 3px;display:flex;justify-content:center;align-items:center;gap:6px;font-size:10px;color:#9a9a9a}
.utility .on{color:#fff}
.search{left:781px;top:32px;width:255px;height:28px;background:#fff;border:1px solid #cfcfcf;border-radius:2px;font-size:10px;font-style:italic;color:#aaa;padding:8px 10px}
.search svg{position:absolute;right:8px;top:6px}

/* navigation */
.nav{left:0;top:69px;width:1200px;height:35px;background:#e6e6e6;border-bottom:1px solid #d8d8d8}
.nav a{position:absolute;top:0;height:35px;line-height:35px;font-size:15px;color:#555;text-decoration:none}
.nav a.current{background:var(--brand);color:#fff;text-align:center;width:83px}

/* featured slider */
.tab{height:46px;line-height:46px;padding-left:22px;font-size:15px;color:#fff}
.feature-tab{left:154px;top:139px;width:181px;background:var(--feature)}
.feature-photo{left:163px;top:178px;width:584px;height:218px;background:radial-gradient(circle at 60% 50%,#f4f4f4,#d7d7d5 70%,#c9c9c6)}
.slide-controls{left:124px;top:396px;width:39px;height:83px;background:var(--brand)}
.caption{left:163px;top:396px;width:584px;height:83px;background:var(--feature);box-shadow:0 8px 10px -6px rgba(0,0,0,.45)}
.model{left:0;top:0;width:192px;height:83px;border-right:1px solid #6c3585;padding:10px 0 0 25px;color:#fff}
.model small{display:block;font-size:14px}
.model strong{display:block;font-size:42px;line-height:46px}
.caption p{position:absolute;left:209px;top:26px;width:360px;font-size:12px;font-weight:700;line-height:16px;color:#c79cd9}

/* latest news */
.news-tab{left:758px;top:138px;width:181px;background:var(--brand-dark)}
.news{left:766px;top:178px;width:271px;height:301px;background:var(--brand);box-shadow:0 8px 10px -6px rgba(0,0,0,.45)}
.news h3{position:absolute;left:17px;top:20px;width:238px;font-size:11px;color:#fff;padding-bottom:8px;border-bottom:1px solid #4f4a9c}
.news-photo{left:18px;top:55px;width:233px;height:106px;background:linear-gradient(90deg,#f6f6f6,#e2e2e2 50%,#f6f6f6)}
.price{left:18px;top:170px;width:233px;height:35px;background:#4540a0;border:1px solid #524da9;display:flex;align-items:center;gap:14px;padding-left:8px}
.price b{font-size:24px;color:#221e66;font-family:"Roboto Condensed",sans-serif}
.price span{font-size:15px;color:#fff}
.news p{position:absolute;left:18px;top:216px;width:233px;font-size:9px;line-height:10px;color:#b9b6e6}

/* markets */
.market{top:522px;width:197px;height:326px;box-shadow:0 9px 10px -6px rgba(0,0,0,.5)}
.market-photo{left:0;top:0;width:197px;height:142px;background:linear-gradient(#f2f2f2,#d9d9d6)}
.market-body{left:0;top:142px;width:197px;height:184px;background:radial-gradient(circle at 30% 45%,#4a4a4a,var(--card) 60%)}
.market-tab{left:-9px;top:102px;width:181px;height:40px;line-height:40px;padding-left:23px;font-size:14px;color:#fff;background:#3b3b3b}
.market-tab::after{content:"";position:absolute;left:0;bottom:-6px;border-left:181px solid var(--card-dark);border-bottom:6px solid transparent}
.market h4{position:absolute;left:10px;top:32px;font-size:11px;color:#fff}
.market p{position:absolute;left:10px;top:49px;width:180px;font-size:11px;line-height:14px;color:#8c8c8c}
.learn{position:absolute;left:12px;top:131px;width:76px;height:21px;line-height:19px;text-align:center;font-size:10px;color:#444;background:linear-gradient(#fff,#cfcfcf);border:1px solid #999;border-radius:2px}

/* footer */
.footer{left:0;top:908px;width:1200px;height:153px;background:var(--band);border-top:1px solid #d6d6d6}
.rule{top:0;width:1px;height:153px;background:#cfcfcf}
.foot-head{top:30px;font-size:14px;color:var(--brand)}
.links a{position:absolute;font-size:10px;color:#555;text-decoration:none;text-transform:uppercase}
.links a.current{background:var(--brand);color:#fff;padding:4px 0 4px 12px;width:87px;margin-top:-4px;margin-left:-1px}
.social{display:flex;align-items:center;gap:9px;font-size:10px;color:#555}
.social i{width:22px;height:22px;border-radius:50%;background:#3d3d3d;display:block}
.social i.hi{background:var(--brand)}
.join{left:816px;top:59px;width:221px;font-size:10px;line-height:14px;color:#555}
.email{left:816px;top:87px;width:221px;height:22px;background:#fff;border:1px solid #cfcfcf}
.subscribe{left:816px;top:118px;width:85px;height:21px;line-height:21px;text-align:center;font-size:10px;color:#fff;background:linear-gradient(#6a66c0,var(--brand));border:1px solid #2a2670}
.bottom{left:0;top:1061px;width:1200px;height:46px;line-height:46px;text-align:center;background:var(--brand);color:#fff;font-size:10px}
</style>
</head>
<body>

<header class="abs masthead">
  <div class="abs brand"><span class="brand-mark"></span><span class="brand-name">Bright Harbor<br>Lighting Systems</span></div>
  <div class="abs utility"><span class="on">About</span>|<span>Why Us</span>|<span>Contact Us</span>|<span>Login</span>|<span>Register</span></div>
  <div class="abs search">Search here...
    <svg width="16" height="16" viewBox="0 0 16 16"><circle cx="6.5" cy="6.5" r="4.5" fill="none" stroke="#666" stroke-width="2"/><path d="M10 10l4.5 4.5" stroke="#666" stroke-width="2.5"/></svg>
  </div>
</header>

<nav class="abs nav cond">
  <a class="current" style="left:164px">Home</a>
  <a style="left:268px">Resume</a>
  <a style="left:355px">Products</a>
  <a style="left:456px">Lighting Design</a>
  <a style="left:595px">Latest News</a>
  <a style="left:719px">Manuals</a>
  <a style="left:819px">Technical</a>
  <a style="left:925px">Contact Us</a>
</nav>

<div class="abs tab feature-tab cond">Featured Products</div>
<div class="abs feature-photo" role="img" aria-label="Photo of an LED lighting module with its white mounting ring and cable"></div>
<div class="abs slide-controls">
  <svg width="39" height="83" viewBox="0 0 39 83">
    <path d="M27 13L15 21L27 29Z" fill="#fff"/>
    <path d="M14 35L26 43L14 51Z" fill="#fff"/>
    <line x1="0" y1="62" x2="39" y2="62" stroke="#4f4a9c"/>
    <rect x="15" y="66" width="3" height="11" fill="#fff"/><rect x="21" y="66" width="3" height="11" fill="#fff"/>
  </svg>
</div>
<div class="abs caption">
  <div class="abs model cond"><small>Model No.</small><strong>2 BL 455</strong></div>
  <p>Lumenford and Corvane roll out Halvia modules to streamline LED lighting integration.</p>
</div>

<div class="abs tab news-tab cond">Latest News</div>
<section class="abs news">
  <h3>Introducing the 4BL455</h3>
  <div class="abs news-photo" role="img" aria-label="Photo of two black LED flood light fixtures"></div>
  <div class="abs price"><b>$ 100.00</b><span class="cond">Save 15% Energy</span></div>
  <p>Lorem Ipsum is simply dummy text of the printing and typesetting industry. Lorem Ipsum has been the industry's standard dummy text ever since the 1500s, when an unknown</p>
  <svg class="abs" style="left:226px;top:336px" width="60" height="16" viewBox="0 0 60 16"><path d="M14 1L2 8L14 15Z" fill="#fff"/><path d="M32 1L44 8L32 15Z" fill="#fff"/></svg>
</section>

<article class="abs market" style="left:162px">
  <div class="abs market-photo" role="img" aria-label="Photo of studio LED panel lights with barn doors"></div>
  <div class="abs market-body"><h4>Public &amp; Commercial</h4><p>Lorem Ipsum is simply dummy text of the printing and typesetting industry. Lorem Ipsum has been the industry's standard dummy text ever since the 1500s, when an unknown</p><span class="learn cond">Learn More</span></div>
  <div class="abs market-tab cond">Broadcasting</div>
</article>
<article class="abs market" style="left:388px">
  <div class="abs market-photo" role="img" aria-label="Photo of hanging fluorescent studio light fixtures"></div>
  <div class="abs market-body"><h4>ISD Wide &amp; Private Schools</h4><p>Lorem Ipsum is simply dummy text of the printing and typesetting industry. Lorem Ipsum has been the industry's standard dummy text ever since the 1500s, when an unknown</p><span class="learn cond">Learn More</span></div>
  <div class="abs market-tab cond">Education</div>
</article>
<article class="abs market" style="left:615px">
  <div class="abs market-photo" role="img" aria-label="Photo of LED tube lights"></div>
  <div class="abs market-body"><h4>National News, Chamber videos</h4><p>Lorem Ipsum is simply dummy text of the printing and typesetting industry. Lorem Ipsum has been the industry's standard dummy text ever since the 1500s, when an unknown</p><span class="learn cond">Learn More</span></div>
  <div class="abs market-tab cond">Government</div>
</article>
<article class="abs market" style="left:840px">
  <div class="abs market-photo" role="img" aria-label="Photo of silver LED flood lights"></div>
  <div class="abs market-body"><h4>Sermon Recording, etc.</h4><p>Lorem Ipsum is simply dummy text of the printing and typesetting industry. Lorem Ipsum has been the industry's standard dummy text ever since the 1500s, when an unknown</p><span class="learn cond">Learn More</span></div>
  <div class="abs market-tab cond">Religious</div>
</article>

<footer class="abs footer">
  <div class="abs rule" style="left:367px"></div>
  <div class="abs rule" style="left:628px"></div>
  <div class="abs rule" style="left:788px"></div>

  <div class="abs foot-head cond" style="left:162px">Site Map</div>
  <div class="links">
    <a style="left:163px;top:61px">About Us</a>
    <a class="current" style="left:163px;top:82px">Resume</a>
    <a style="left:163px;top:103px">Products</a>
    <a style="left:163px;top:124px">Lighting Design</a>
    <a style="left:272px;top:61px">Latest News</a>
    <a style="left:272px;top:82px">Manuals</a>
    <a style="left:272px;top:103px">Technical</a>
    <a style="left:272px;top:124px">Contact Us</a>
  </div>

  <div class="abs foot-head cond" style="left:392px">Products</div>
  <div class="links">
    <a style="left:393px;top:61px">Accent Lights</a>
    <a style="left:393px;top:82px">Fill Lights</a>
    <a style="left:393px;top:103px">Small Studio</a>
    <a style="left:393px;top:124px">Video Conferencing</a>
    <a style="left:533px;top:61px">Accessories</a>
    <a style="left:533px;top:82px">Dimming</a>
    <a style="left:533px;top:103px">Portable</a>
    <a style="left:533px;top:124px">Fancy</a>
  </div>

  <div class="abs foot-head cond" style="left:658px">Follow Us</div>
  <div class="abs social" style="left:656px;top:52px"><i class="hi"></i>BECOME A FAN</div>
  <div class="abs social" style="left:656px;top:83px"><i></i>FOLLOW US ON</div>
  <div class="abs social" style="left:656px;top:114px"><i></i>JOIN US</div>

  <div class="abs foot-head cond" style="left:816px">Join Our Email List</div>
  <p class="abs join">LOREM IPSUM IS SIMPLY DUMMY TEXT OF THE PRINTING AND TYPESETTING INDUSTRY.</p>
  <div class="abs email"></div>
  <div class="abs subscribe cond">Subscribe</div>
</footer>

<div class="abs bottom">Copyrights © BrightHarbor.example</div>

</body>
</html>
```